Shampoo and Shower Gel Packaging Design

I need a new packaging design for a men shampoo and shower gel bottle. The packaging must me black (black bottle/package) and the logo should be also monochrom.
For example, black matte bottle and black shiny logo on the packaging (not mandatory).
the design must contain maximum 3 colors.
1. black
2. white (text)
3. grey/dark blue/dark green (colors will be the difference between products parfumes/smell/scences.

Design must be minimalist/elegant/discrete.
Updates

Please check the photos i added for pure inspiration.

Target Market(s)

brand exclusively for MEN - premium clients

Industry/Entity Type

Cosmetics

Font styles to use
Sans Serif

Colors
1b1b1b
5c5c5c
aaaaaa
ffffff
3176b5

Requirements
Must have
• black background
• minimalist design

```html
<!DOCTYPE html>
<html lang="en">
<head>
<meta charset="utf-8">
<title>Men's Shampoo Range</title>
<link href="https://fonts.googleapis.com/css2?family=Questrial&display=swap" rel="stylesheet">
<style>
  :root {
    --page: #ffffff;
    --bottle-dark: #262626;
    --bottle-mid: #3b3b3b;
    --bottle-edge: #1b1b1b;
    --collar-light: #d9d9d9;
    --collar-mid: #bdbdbd;
    --pump: #1b1b1b;
    --pump-top: #5c5c5c;
    --label-text: #ffffff;
    --scent-green: #3aa845;
    --scent-grey: #aaaaaa;
    --scent-blue: #3176b5;
  }
  * { margin: 0; padding: 0; box-sizing: border-box; }
  html, body { width: 1200px; height: 848px; overflow: hidden; background: var(--page); }
  body { position: relative; font-family: "Questrial", "Century Gothic", sans-serif; color: var(--label-text); }

  .bottle { position: absolute; top: 0; width: 200px; height: 848px; }
  .bottle--one { left: 193px; --scent: var(--scent-green); }
  .bottle--two { left: 497px; --scent: var(--scent-grey); }
  .bottle--three { left: 800px; --scent: var(--scent-blue); }
  .bottle__shape { position: absolute; left: 0; top: 0; width: 200px; height: 848px; }

  .product-mark { position: absolute; left: 32px; top: 332px; width: 140px; height: 56px; }
  .product-mark__dot { position: absolute; left: 8px; top: 10px; width: 22px; height: 22px; border-radius: 50%; background: var(--scent); }
  .product-mark__name { position: absolute; left: 38px; top: 2px; font-size: 27px; line-height: 30px; }
  .product-mark__type { position: absolute; left: 54px; top: 31px; font-size: 11px; line-height: 13px; }
  .product-mark__rule { position: absolute; left: 34px; top: 50px; width: 100px; height: 2px; background: var(--scent); }

  .scent-info { position: absolute; left: 0; width: 200px; top: 434px; text-align: center; font-size: 11.5px; line-height: 25px; }

  .brand { position: absolute; left: 0; width: 200px; top: 540px; text-align: center; }
  .brand__dot { display: block; width: 20px; height: 20px; margin: 0 auto 10px; border-radius: 50%; background: var(--label-text); }
  .brand__name { display: block; font-size: 21px; letter-spacing: 9px; padding-left: 9px; line-height: 22px; }
  .brand__sub { display: block; font-size: 5px; letter-spacing: 2.4px; padding-left: 2px; line-height: 8px; }

  .volume { position: absolute; left: 74px; top: 677px; width: 52px; height: 24px; border: 1px solid var(--label-text); border-radius: 50%; font-size: 10px; line-height: 22px; text-align: center; }
</style>
</head>
<body>

<svg width="0" height="0" style="position:absolute" aria-hidden="true">
  <defs>
    <linearGradient id="body-shade" x1="0" x2="1" y1="0" y2="0">
      <stop offset="0" stop-color="#1e1e1e"/>
      <stop offset="0.35" stop-color="#3a3a3a"/>
      <stop offset="0.75" stop-color="#333333"/>
      <stop offset="1" stop-color="#1b1b1b"/>
    </linearGradient>
    <linearGradient id="collar-shade" x1="0" x2="1" y1="0" y2="0">
      <stop offset="0" stop-color="#bdbdbd"/>
      <stop offset="0.4" stop-color="#dedede"/>
      <stop offset="1" stop-color="#b5b5b5"/>
    </linearGradient>
    <symbol id="bottle-shape" viewBox="0 0 200 848">
      <path d="M17 262 Q17 250 100 250 Q183 250 183 262 L183 700 Q183 718 100 718 Q17 718 17 700 Z" fill="url(#body-shade)"/>
      <path d="M50 178 L152 178 L152 252 Q152 262 101 262 Q50 262 50 252 Z" fill="url(#collar-shade)"/>
      <rect x="65" y="150" width="72" height="28" fill="#1b1b1b"/>
      <rect x="70" y="136" width="62" height="16" fill="#2a2a2a"/>
      <path d="M24 130 L40 118 L134 118 L134 140 L46 140 L32 148 L24 142 Z" fill="#1b1b1b"/>
      <path d="M40 118 L134 118 L134 124 L38 124 Z" fill="#5c5c5c"/>
    </symbol>
  </defs>
</svg>

<article class="bottle bottle--one">
  <svg class="bottle__shape" viewBox="0 0 200 848" aria-hidden="true"><use href="#bottle-shape"/></svg>
  <div class="product-mark">
    <span class="product-mark__dot"></span>
    <span class="product-mark__name">Name</span>
    <span class="product-mark__type">Shampoo</span>
    <span class="product-mark__rule"></span>
  </div>
  <p class="scent-info">For Men<br>with<br>Fragrance 1</p>
  <div class="brand"><span class="brand__dot"></span><span class="brand__name">VERNO</span><span class="brand__sub">COSMETICS</span></div>
  <div class="volume">200 ml</div>
</article>

<article class="bottle bottle--two">
  <svg class="bottle__shape" viewBox="0 0 200 848" aria-hidden="true"><use href="#bottle-shape"/></svg>
  <div class="product-mark">
    <span class="product-mark__dot"></span>
    <span class="product-mark__name">Name</span>
    <span class="product-mark__type">Shampoo</span>
    <span class="product-mark__rule"></span>
  </div>
  <p class="scent-info">For Men<br>with<br>Fragrance 2</p>
  <div class="brand"><span class="brand__dot"></span><span class="brand__name">VERNO</span><span class="brand__sub">COSMETICS</span></div>
  <div class="volume">200 ml</div>
</article>

<article class="bottle bottle--three">
  <svg class="bottle__shape" viewBox="0 0 200 848" aria-hidden="true"><use href="#bottle-shape"/></svg>
  <div class="product-mark">
    <span class="product-mark__dot"></span>
    <span class="product-mark__name">Name</span>
    <span class="product-mark__type">Shampoo</span>
    <span class="product-mark__rule"></span>
  </div>
  <p class="scent-info">For Men<br>with<br>Fragrance 3</p>
  <div class="brand"><span class="brand__dot"></span><span class="brand__name">VERNO</span><span class="brand__sub">COSMETICS</span></div>
  <div class="volume">200 ml</div>
</article>

</body>
</html>
```